Design of a nice Video On Demand Website

We are looking to design a nice Website for our Video On demand platform we are getting ready to launch. We have put together a file to illustrate the idea and design concept we want. The file also has the menu sections ect. The Designers should look at the file and suggest design ideas based on the concept we put together on the file. The design should be clean yet simple so users can experience a better Navigation. The designer is free to choose whatever color he thinks fit.
Updates

Need extra days to review

Sick

Target Market(s)

Streaming

Number of Pages Required

1 page

Font styles to use
Sans Serif

Colors

Designer to choose colors to be used in the design.

Requirements
Must have
• I will let the designer choose what is best.
Nice to have
• N/A
Should not have
• N/A

```html
<!DOCTYPE html>
<html lang="en">
<head>
<meta charset="utf-8">
<title>KORA – Video On Demand</title>
<link rel="stylesheet" href="https://fonts.googleapis.com/css2?family=Nunito+Sans:wght@300;400;700;800;900&display=swap">
<style>
  :root{
    --bg:#1b1c1e;
    --bar:rgba(40,42,45,.92);
    --side:rgba(22,23,25,.82);
    --accent:#e8652c;
    --live:#2fb34a;
    --white:#ffffff;
    --muted:#a9abad;
    --menu:#e9e9e9;
  }
  *{box-sizing:border-box;margin:0;padding:0}
  html,body{width:1200px;height:656px;overflow:hidden;background:var(--bg);font-family:"Nunito Sans",sans-serif}
  .screen{position:relative;width:1200px;height:656px;overflow:hidden}
  .hero-photo{position:absolute;inset:0;
    background:
      radial-gradient(ellipse 260px 220px at 830px 500px, rgba(255,150,30,.85), rgba(230,90,20,.35) 55%, transparent 75%),
      radial-gradient(ellipse 230px 320px at 600px 380px, rgba(235,235,235,.85), rgba(200,200,200,.4) 55%, transparent 80%),
      radial-gradient(ellipse 140px 200px at 360px 380px, rgba(210,210,210,.45), transparent 75%),
      linear-gradient(180deg,#6b7074 0%,#8a8f93 35%,#545a5f 70%,#2c2f32 100%);}
  .topbar{position:absolute;left:0;top:0;width:1200px;height:51px;background:var(--bar)}
  .brand{position:absolute;left:16px;top:12px;display:flex;align-items:center;gap:6px}
  .brand-mark{width:14px;height:14px;background:var(--accent)}
  .brand-name{color:var(--white);font-weight:900;font-size:22px;line-height:26px;letter-spacing:.5px}
  .channels{position:absolute;left:256px;top:0;height:51px;display:flex;align-items:center;gap:34px;list-style:none}
  .channels li{color:var(--muted);font-weight:800;font-size:17px;white-space:nowrap}
  .search{position:absolute;right:26px;top:15px}
  .sidebar{position:absolute;left:0;top:51px;width:254px;height:605px;background:var(--side)}
  .live{position:absolute;left:16px;top:26px;width:70px;height:26px;background:var(--live);border-radius:2px;color:var(--white);font-weight:800;font-size:14px;display:flex;align-items:center;gap:6px;padding-left:9px}
  .live::before{content:"";width:10px;height:10px;border-radius:50%;background:#7fe38f}
  .menu{position:absolute;left:0;top:67px;width:254px;list-style:none}
  .menu li{height:44px;display:flex;align-items:center;gap:11px;padding-left:11px;color:var(--menu);font-weight:800;font-size:14.5px;letter-spacing:.2px;white-space:nowrap}
  .menu li.active{background:var(--accent);color:var(--white)}
  .menu svg{width:20px;height:20px;flex:none}
  .promo{position:absolute;left:72px;top:530px;width:96px;text-align:center;color:#e9b520;font-weight:900;font-size:22px}
  .hero-title{position:absolute;left:810px;top:110px;color:var(--white);font-weight:900;font-size:46px;line-height:48px;letter-spacing:-.5px;white-space:nowrap}
  .hero-sub{position:absolute;left:810px;top:174px;width:340px;color:var(--white);font-weight:900;font-size:21px;line-height:25px}
  .hero-desc{position:absolute;left:810px;top:233px;width:360px;color:var(--white);font-weight:300;font-size:19px;line-height:24px}
  .cta{position:absolute;left:813px;top:301px;width:187px;height:49px;background:var(--accent);border-radius:2px;display:flex;align-items:center;gap:10px;padding-left:16px;color:var(--white);font-weight:900;font-size:17px}
  .footer{position:absolute;left:344px;top:622px;width:738px;height:34px;background:rgba(25,26,28,.75);display:flex;align-items:center;justify-content:center;color:var(--white);font-size:12px;white-space:nowrap}
  .code{position:absolute;right:6px;bottom:3px;color:var(--white);font-size:11px}
</style>
</head>
<body>
<div class="screen">
  <div class="hero-photo" role="img" aria-label="Photo of chefs cooking in a professional kitchen, one flambéing a pan with large flames"></div>

  <header class="topbar">
    <div class="brand"><span class="brand-mark"></span><span class="brand-name">KORA</span></div>
    <ul class="channels">
      <li>Onde 5</li><li>Radio Vue</li><li>Radio Lagune</li><li>KORA Nord</li><li>KORA 1</li><li>KORA 2</li><li>KORA 3</li><li>KORA.news</li>
    </ul>
    <svg class="search" width="20" height="20" viewBox="0 0 20 20" fill="none" stroke="#fff" stroke-width="2.6"><circle cx="8" cy="8" r="6"/><path d="M12.5 12.5 18 18" stroke-linecap="round"/></svg>
  </header>

  <nav class="sidebar">
    <div class="live">LIVE</div>
    <ul class="menu">
      <li><svg viewBox="0 0 20 20" fill="#fff"><circle cx="10" cy="6" r="4"/><path d="M2 19c0-5 4-7 8-7s8 2 8 7z"/></svg>MY ACCOUNT</li>
      <li class="active"><svg viewBox="0 0 20 20" fill="#fff"><circle cx="6" cy="8" r="4"/><circle cx="14" cy="8" r="4"/><circle cx="10" cy="6" r="5"/><rect x="5" y="11" width="10" height="6" rx="1"/></svg>GRILLS DES PROGRAMMES</li>
      <li><svg viewBox="0 0 20 20" fill="#fff"><path d="M3 3l14 6-6 2-2 6z"/></svg>MY SELECTION</li>
      <li><svg viewBox="0 0 20 20" fill="none" stroke="#fff" stroke-width="2"><circle cx="9" cy="10" r="7"/><circle cx="9" cy="6" r="1.5" fill="#fff"/><circle cx="5.5" cy="11" r="1.5" fill="#fff"/><circle cx="12.5" cy="11" r="1.5" fill="#fff"/><path d="M14 16h5"/></svg>ENTERTAINMENT</li>
      <li><svg viewBox="0 0 20 20" fill="#fff"><path d="M2 4h10v7a5 5 0 0 1-10 0z"/><path d="M10 6h8v6a4 4 0 0 1-8 0z" opacity=".7"/></svg>SERIES</li>
      <li><svg viewBox="0 0 20 20" fill="none" stroke="#fff" stroke-width="1.8"><rect x="2" y="3" width="16" height="11" rx="1"/><path d="M7 18h6M8 6l4 2.5L8 11z"/></svg>TV MOVIES</li>
      <li><svg viewBox="0 0 20 20" fill="none" stroke="#fff" stroke-width="1.8"><circle cx="10" cy="10" r="8"/><path d="M10 9v5M10 6v.5" stroke-linecap="round"/></svg>INFO &amp; COMPNAY</li>
      <li><svg viewBox="0 0 20 20" fill="none" stroke="#fff" stroke-width="1.8"><circle cx="10" cy="10" r="8"/><path d="M10 6l3 2-1 4H8l-1-4z" fill="#fff"/></svg>SPORT</li>
      <li><svg viewBox="0 0 20 20" fill="none" stroke="#fff" stroke-width="1.8"><circle cx="10" cy="10" r="8"/><path d="M5 10h10a5 5 0 0 1-10 0z"/></svg>HUMOR</li>
      <li><svg viewBox="0 0 20 20" fill="#fff"><circle cx="10" cy="6" r="4"/><path d="M3 19c0-5 3-7 7-7s7 2 7 7z"/></svg>YOUTH</li>
    </ul>
    <div class="promo">FLIPO II</div>
  </nav>

  <h1 class="hero-title">CHEF ROYAL</h1>
  <h2 class="hero-sub">THE MODERN CASSEROLE OF<br>MARC AUBERTIN</h2>
  <p class="hero-desc">Candidates are Supported by<br>Paul Delorme</p>
  <a class="cta"><svg width="21" height="21" viewBox="0 0 21 21"><circle cx="10.5" cy="10.5" r="10.5" fill="#fff"/><path d="M8 6l6 4.5L8 15z" fill="#e8652c"/></svg>SEE THE VIDEO</a>

  <footer class="footer">Mentions Legales&nbsp; | &nbsp;Conditions generales dutilisation&nbsp; | &nbsp;Politique de protection des donness personnelles&nbsp; | &nbsp;Cookies&nbsp; | &nbsp;CGU&nbsp; | Contacts</footer>
  <span class="code">X37</span>
</div>
</body>
</html>
```